Luxury packaging graphic design for a new Hair care elixir

We need a packaging design for a new product for our line extension of hair colouring. We have already a packaging that is very well received (all in pink) including all accesories and transport box (attached files).
For a new product - protein for the hair - we need a different design tapping into luxury segment.

Target Market(s)

This product is mainly for women between 25-65 that are looking forward to improve hair strukture and make hair looks better, nicer, softer, healthier. The product in the packaging could be used up to 2x times.

Industry/Entity Type

Hair And Beauty

Font styles to use
Serif
Sans Serif

Colors

Designer to choose colors to be used in the design.

Requirements
Must have
• The material of the packaging are carton/styropor/and glass (attached a picture of packaging design to be adapted). The components are quite small so the packaging plays a big role to increase the value of what it is inside. The packaging needs to be inline with our actual packaging designs and corporate identity as they may be delivered together so as an assamble it should look nice, beautiful and of high quality.
• The graphic design for the different components to be adapted are:
• - grapich design for outside box
• - graphic design for the inside bottles
• - graphic design for the flyer/instructions inside the box
Nice to have
• It needs to feel that the packaging is Wow! It is going to be delivered per post so there have to be a beautiful opening effect. Eventually to work with colours like black, white and gold would give a nice luxury feeling.
• The actual product inside is a concentrated protein component so it is very small, therefore the packaging should show that even if small it is an elixir for the hair.
Should not have
• a totally diffenet look as our actual designs.

```html
<!DOCTYPE html>
<html lang="en">
<head>
<meta charset="utf-8">
<title>Nova Elle – Amber Glow packaging</title>
<link rel="stylesheet" href="https://fonts.googleapis.com/css2?family=Montserrat:wght@400;500&display=swap">
<style>
  :root {
    --backdrop: #ead3c2;
    --paper: #ffffff;
    --copper-line: #e39a5f;
    --gold-a: #b9862f;
    --gold-b: #f2d98a;
    --ink: #1b1b1b;
    --ink-soft: #4a4a4a;
    --bottle-top: #a9784f;
    --bottle-mid: #c08e63;
    --bottle-low: #b07a4d;
    --cap-a: #c8b08d;
    --cap-b: #efe0c4;
    --label-light: #f3c9a2;
    --label-dark: #3b2617;
  }
  * { margin: 0; padding: 0; box-sizing: border-box; }
  html, body { width: 1200px; height: 828px; overflow: hidden; }
  body {
    position: relative;
    background: var(--backdrop);
    font-family: "Montserrat", sans-serif;
  }

  /* ---------- Box lid ---------- */
  .box-lid {
    position: absolute;
    left: 128px; top: 169px;
    width: 467px; height: 471px;
    background: var(--paper);
    border: 1px solid #d9cfc6;
  }
  .box-lid .brand {
    position: absolute; left: 0; right: 0; top: 40px;
    text-align: center;
    font-weight: 500; font-size: 20px; letter-spacing: 3px;
    color: var(--ink);
  }
  .box-lid .tagline {
    position: absolute; left: 0; right: 0; top: 69px;
    text-align: center; font-size: 7px; letter-spacing: 1.6px;
    color: var(--ink-soft);
  }
  .box-lid .gold-band {
    position: absolute; left: 2px; right: 2px; top: 90px; height: 4px;
    background: linear-gradient(90deg, var(--gold-a), var(--gold-b));
  }
  .box-lid .product-name {
    position: absolute; left: 0; right: 0; top: 106px;
    text-align: center; font-size: 20px; font-weight: 400;
    letter-spacing: 0.4px; color: var(--ink);
  }
  .box-lid .emblem {
    position: absolute; left: 138px; top: 143px;
    width: 184px; height: 184px;
  }
  .box-lid .claims { position: absolute; left: 2px; right: 2px; top: 336px; }
  .claim {
    text-align: center; font-size: 6.5px; line-height: 8px;
    letter-spacing: 0.6px; color: var(--ink-soft);
    border-bottom: 1.5px solid var(--copper-line);
  }
  .claim.first { height: 23px; }
  .claim.second { height: 36px; padding-top: 12px; }
  .claim.third { height: 32px; padding-top: 9px; }
  .box-lid .volume {
    position: absolute; left: 0; right: 0; top: 437px;
    text-align: center; font-size: 7px; letter-spacing: 0.6px;
    color: var(--ink-soft);
  }

  /* ---------- Bottle ---------- */
  .bottle { position: absolute; left: 776px; top: 218px; width: 110px; height: 360px; }
  .bottle .cap {
    position: absolute; left: 38px; top: 0; width: 36px; height: 42px;
    border-radius: 3px 3px 0 0;
    background: linear-gradient(90deg, var(--cap-a), var(--cap-b) 60%, var(--cap-a));
  }
  .bottle .body {
    position: absolute; left: 0; top: 42px; width: 110px; height: 318px;
    border-radius: 34px 34px 10px 10px;
    background: linear-gradient(180deg, var(--bottle-top), var(--bottle-mid) 45%, var(--bottle-low));
  }
  .label { position: absolute; left: 0; right: 0; text-align: center; }
  .label.brand {
    top: 50px; font-weight: 500; font-size: 10px; letter-spacing: 1.5px;
    color: var(--label-light);
  }
  .label.tagline { top: 67px; font-size: 4px; letter-spacing: 1px; color: var(--label-light); }
  .label.rule { top: 82px; height: 2px; background: linear-gradient(90deg, var(--gold-a), var(--gold-b)); }
  .label.rule.thin { top: 242px; height: 1px; }
  .label.name { top: 142px; font-size: 7.5px; font-weight: 500; color: var(--label-light); }
  .label.claim-de { top: 229px; font-size: 4px; line-height: 5px; font-weight: 500; color: var(--label-dark); }
  .label.size { top: 253px; font-size: 4px; color: var(--label-dark); }
  .bottle .mini-emblem { position: absolute; left: 35px; top: 99px; width: 40px; height: 40px; }
</style>
</head>
<body>

  <section class="box-lid">
    <div class="brand">NOVA ELLE</div>
    <div class="tagline">SHADES MADE FOR YOU</div>
    <div class="gold-band"></div>
    <h1 class="product-name">AMBER GLOW</h1>
    <svg class="emblem" viewBox="0 0 184 184" role="img" aria-label="Line-art sphere of flowing hair strands in copper">
      <circle cx="92" cy="92" r="90" fill="#f6dcc6"/>
    </svg>
    <div class="claims">
      <div class="claim first">STRAHLENDE FÄRBENDE<br>BEHANDLUNG</div>
      <div class="claim second">TRAITEMENT DE<br>COLORATION ÉCLANTE</div>
      <div class="claim third">RADIANT COLORING<br>TREATMENT</div>
    </div>
    <div class="volume">1:1 60ML ℮</div>
  </section>

  <section class="bottle">
    <div class="cap"></div>
    <div class="body">
      <div class="label brand">NOVA ELLE</div>
      <div class="label tagline">SHADES MADE FOR YOU</div>
      <div class="label rule"></div>
      <svg class="mini-emblem" viewBox="0 0 40 40" role="img" aria-label="Small hair-strand sphere emblem">
        <circle cx="20" cy="20" r="19" fill="#d9a57a"/>
      </svg>
      <div class="label name">Amber glow</div>
      <div class="label claim-de">STRAHLENDE FÄRBENDE<br>BEHANDLUNG</div>
      <div class="label rule thin"></div>
      <div class="label size">100 ml</div>
    </div>
  </section>

</body>
</html>
```